Harbor Fieldworks (Business Card Design)

Need business cards designed. Something modern, chic, and sleek. Mabye the back of the card should be the navy blue that is in the logo and then just the logo on the back.

Target Market(s)

Those in the hotel, office, and renovation industry

Contact Information for Business Card

1. Logo 2. Dorian Velasko 3. CEO/Founder 4. Phone: (833) HarbFld / (833) 427-2353 5. Email: dorian@theharborfieldworks.com 6. Website: www.theharborfieldworks.com

Font styles to use
Other font styles liked:
• Look at the logo font and base the font for everything else off of that.

Colors
0054AA
0677BA
7BADD7
CADEEF
E8F1F8

Requirements
Must have
• Colors that are associated in the logo
Nice to have
• Sleek modern clean and chic design.

```html
<!DOCTYPE html>
<html lang="en">
<head>
<meta charset="utf-8">
<title>Harbor Fieldworks — Business Cards</title>
<link rel="stylesheet" href="https://fonts.googleapis.com/css2?family=Montserrat:wght@600;700&family=Open+Sans:wght@400&display=swap">
<style>
  :root {
    --backdrop: #2d2d2d;
    --navy: #0c1a42;
    --gold: #c9a13f;
    --white: #ffffff;
  }
  * { box-sizing: border-box; margin: 0; padding: 0; }
  html, body {
    width: 1200px;
    height: 1015px;
    overflow: hidden;
    background: var(--backdrop);
  }
  .sheet {
    width: 1200px;
    height: 1015px;
    display: flex;
    flex-direction: column;
    align-items: center;
    justify-content: center;
    gap: 44px;
  }
  .card {
    position: relative;
    width: 700px;
    height: 400px;
    background: var(--navy);
    overflow: hidden;
    box-shadow: 0 10px 24px rgba(0,0,0,0.45);
  }
  .card__band {
    position: absolute;
    left: 0; right: 0; bottom: 0;
    height: 22px;
    background: var(--gold);
  }

  /* Front */
  .card--front {
    display: flex;
    align-items: center;
    justify-content: center;
  }
  .wordmark {
    display: flex;
    align-items: center;
    gap: 18px;
    margin-bottom: 22px;
  }
  .wordmark__square {
    width: 22px;
    height: 22px;
    background: var(--gold);
  }
  .wordmark__name {
    font-family: "Montserrat", sans-serif;
    font-weight: 700;
    font-size: 40px;
    letter-spacing: 4px;
    color: var(--white);
    text-transform: uppercase;
  }

  /* Back */
  .holder {
    position: absolute;
    left: 48px;
    top: 96px;
  }
  .holder__name {
    font-family: "Montserrat", sans-serif;
    font-weight: 700;
    font-size: 30px;
    letter-spacing: 0.5px;
    color: var(--white);
    text-transform: uppercase;
    line-height: 1.1;
  }
  .holder__role {
    font-family: "Open Sans", sans-serif;
    font-size: 17px;
    color: var(--gold);
    text-transform: uppercase;
    margin-top: 2px;
  }
  .brand-mark {
    position: absolute;
    right: 44px;
    top: 60px;
    display: flex;
    align-items: center;
    gap: 12px;
  }
  .brand-mark__square {
    width: 16px;
    height: 16px;
    background: var(--gold);
  }
  .brand-mark__name {
    font-family: "Montserrat", sans-serif;
    font-weight: 700;
    font-size: 22px;
    letter-spacing: 2px;
    color: var(--white);
    text-transform: uppercase;
  }
  .contacts {
    position: absolute;
    left: 48px;
    bottom: 58px;
    list-style: none;
    display: flex;
    flex-direction: column;
    gap: 10px;
  }
  .contacts__item {
    display: flex;
    align-items: center;
    gap: 12px;
    font-family: "Open Sans", sans-serif;
    font-size: 19px;
    color: var(--white);
  }
  .contacts__icon {
    width: 20px;
    height: 20px;
    flex: none;
  }
</style>
</head>
<body>
<main class="sheet">
  <section class="card card--front" aria-label="Card front">
    <div class="wordmark">
      <span class="wordmark__square"></span>
      <span class="wordmark__name">Harbor Fieldworks</span>
    </div>
    <div class="card__band"></div>
  </section>

  <section class="card card--back" aria-label="Card back">
    <div class="brand-mark">
      <span class="brand-mark__square"></span>
      <span class="brand-mark__name">Harbor Fieldworks</span>
    </div>

    <div class="holder">
      <h1 class="holder__name">Dorian Velasko</h1>
      <p class="holder__role">CEO/Founder</p>
    </div>

    <ul class="contacts">
      <li class="contacts__item">
        <svg class="contacts__icon" viewBox="0 0 24 24" aria-hidden="true">
          <path fill="var(--gold)" d="M6.6 10.8a15.1 15.1 0 0 0 6.6 6.6l2.2-2.2c.3-.3.7-.4 1-.2 1.1.4 2.3.6 3.6.6.6 0 1 .4 1 1V20c0 .6-.4 1-1 1A17 17 0 0 1 3 4c0-.6.4-1 1-1h3.5c.6 0 1 .4 1 1 0 1.3.2 2.5.6 3.6.1.3 0 .7-.2 1z"/>
        </svg>
        <span>(833) HarbFld / (833) 427-2353</span>
      </li>
      <li class="contacts__item">
        <svg class="contacts__icon" viewBox="0 0 24 24" aria-hidden="true">
          <rect x="2" y="5" width="20" height="14" fill="var(--gold)"/>
          <path d="M2 5l10 8 10-8" fill="none" stroke="var(--navy)" stroke-width="1.6"/>
        </svg>
        <span>dorian@theharborfieldworks.com</span>
      </li>
      <li class="contacts__item">
        <svg class="contacts__icon" viewBox="0 0 24 24" aria-hidden="true">
          <g fill="none" stroke="var(--gold)" stroke-width="1.8">
            <circle cx="12" cy="12" r="9"/>
            <ellipse cx="12" cy="12" rx="4" ry="9"/>
            <path d="M3 12h18M5 7h14M5 17h14"/>
          </g>
        </svg>
        <span>www.theharborfieldworks.com</span>
      </li>
    </ul>
    <div class="card__band"></div>
  </section>
</main>
</body>
</html>
```